Construction Company Business Card & Stationary
Brovella Concrete
Construction Company Business Card & Stationary - Construction
Creative Brief
Professional
MARCUS DELWYN JR.
Owner
P.O. Box 482 913 Tamsworth Ridge Lane Medford, NJ 08067
MarcusJr@Brovella.com
www.Brovella.com

```html
<!DOCTYPE html>
<html lang="en">
<head>
<meta charset="utf-8">
<title>Brovella Concrete – Business Card</title>
<link href="https://fonts.googleapis.com/css2?family=Open+Sans:wght@400;600;800&display=swap" rel="stylesheet">
<style>
  :root {
    --backdrop: #2a2c2f;
    --card: #ffffff;
    --ink: #1b1b1b;
    --muted: #555555;
    --rule: #9a9a9a;
  }
  * { margin: 0; padding: 0; box-sizing: border-box; }
  html, body { width: 1200px; height: 901px; overflow: hidden; }
  body {
    background: var(--backdrop);
    font-family: "Open Sans", Arial, sans-serif;
    color: var(--ink);
    display: flex;
    align-items: center;
    justify-content: center;
    gap: 60px;
  }
  .card {
    position: relative;
    width: 525px;
    height: 300px;
    background: var(--card);
    border-radius: 14px;
  }
  .wordmark {
    font-weight: 800;
    text-transform: uppercase;
    line-height: 1;
    color: var(--ink);
  }
  .tagline {
    font-weight: 600;
    text-transform: uppercase;
    letter-spacing: 1.5px;
    color: var(--ink);
  }
  /* Front */
  .card--front .brand {
    position: absolute;
    left: 0; right: 0; top: 92px;
    text-align: center;
  }
  .card--front .wordmark { font-size: 40px; letter-spacing: 1px; }
  .card--front .wordmark .sub { display: block; font-size: 22px; letter-spacing: 6px; margin-top: 6px; }
  .card--front .tagline { font-size: 11px; margin-top: 12px; }
  .card--front .web {
    position: absolute; left: 40px; bottom: 34px;
    font-size: 11px; color: var(--muted);
  }
  /* Back */
  .card--back .brand {
    position: absolute; left: 40px; top: 36px;
  }
  .card--back .wordmark { font-size: 26px; }
  .card--back .wordmark .sub { font-size: 14px; letter-spacing: 4px; margin-left: 8px; }
  .card--back .tagline { font-size: 7px; margin-top: 5px; }
  .card--back .top-rule {
    position: absolute; left: 40px; right: 40px; top: 100px;
    height: 1px; background: var(--ink);
  }
  .address {
    position: absolute; left: 40px; width: 200px; top: 130px;
    text-align: right; font-size: 11px; line-height: 1.55; color: var(--muted);
    font-style: normal;
  }
  .divider {
    position: absolute; left: 262px; top: 122px; bottom: 48px;
    width: 1px; background: var(--rule);
  }
  .contact {
    position: absolute; left: 284px; right: 40px; top: 124px;
    text-align: right;
  }
  .contact .name { font-size: 17px; font-weight: 600; }
  .contact .role { font-size: 11px; color: var(--muted); margin-bottom: 12px; }
  .contact ul { list-style: none; font-size: 10.5px; line-height: 1.7; color: var(--muted); }
  .contact li { display: flex; justify-content: flex-end; align-items: center; gap: 7px; }
  .contact svg { width: 10px; height: 10px; flex: none; }
</style>
</head>
<body>
  <section class="card card--front">
    <div class="brand">
      <div class="wordmark">Brovella<span class="sub">Concrete</span></div>
      <div class="tagline">Strength poured into every project</div>
    </div>
    <div class="web">www.Brovella.com</div>
  </section>

  <section class="card card--back">
    <div class="brand">
      <div class="wordmark">Brovella<span class="sub">Concrete</span></div>
      <div class="tagline">Strength poured into every project</div>
    </div>
    <div class="top-rule"></div>
    <address class="address">
      P.O. Box 482<br>913 Tamsworth Ridge Lane<br>Larkfield, DE 19967
    </address>
    <div class="divider"></div>
    <div class="contact">
      <div class="name">Marcus Delwyn Jr</div>
      <div class="role">Owner</div>
      <ul>
        <li>609-555-0148 <svg viewBox="0 0 10 10"><rect x="2.5" y="0.5" width="5" height="9" rx="1" fill="none" stroke="#1b1b1b"/></svg></li>
        <li>609-555-0172 <svg viewBox="0 0 10 10"><rect x="0.5" y="2" width="9" height="7" fill="none" stroke="#1b1b1b"/><rect x="2.5" y="0.5" width="5" height="2" fill="#1b1b1b"/></svg></li>
        <li>609-555-0193 <svg viewBox="0 0 10 10"><rect x="1" y="1" width="8" height="8" fill="#1b1b1b"/></svg></li>
        <li>MarcusJr@Brovella.com <svg viewBox="0 0 10 10"><rect x="0.5" y="1.5" width="9" height="7" fill="none" stroke="#1b1b1b"/><path d="M0.5 1.5 L5 5.5 L9.5 1.5" fill="none" stroke="#1b1b1b"/></svg></li>
        <li>www.Brovella.com <svg viewBox="0 0 10 10"><circle cx="5" cy="5" r="4.5" fill="none" stroke="#1b1b1b"/><path d="M0.5 5 H9.5 M5 0.5 C2 3 2 7 5 9.5 C8 7 8 3 5 0.5" fill="none" stroke="#1b1b1b"/></svg></li>
      </ul>
    </div>
  </section>
</body>
</html>
```